Velkor Metrics Business Card project

We need a Business Card design for a brand new company called Velkor Metrics, based in Colombia, South America. In spanish, the name Velkor Metrics is built from Describing a Story with Data (Tejer OTRA Fábula con Cifras).
We recently finished our new logo project and now we need the business cards.
In VELKOR we generate knowledge from data. By producing an INTELLIGENT VISUALIZATION of our clients´ data we create AWARENESS of their business environment. We drive GROWTH through DATA VISUALIZATION.
We are a service provider of Data Science, Business Intelligence and Visualization and we are breaking mental barriers in our culture and our market. It is an innovative way to use this services procuring mid term contracts to take our clients in a data based journey to understand their environment. We awe our clients with our data driven insights and our state of the art visualizations
We would like our clients to be seen as: Knowledgable, Dynamic, Fresh, Smart, Acute, Open minded, Brainy, Evolving
Our core has this 4 words: Visual, Knowledgable, Mathematician, Genius
Our brand personality is: Young (early 30s), Brainy, Easy going, Street smart, Creative, Mind blowing, Very Techie, Fun, Social, Uncomplicated
Our promise: we deliver data driven insights using state-of-the-art computer modeling and creative analysis.
This is the first step and the milestone to build all our graphic future (website, mail signature, banners, envelopes, Templates, etc)
It is a face to face sale with cloud based reports and visualizations
There is a similar company that has done great and we want to emulate but we must be different: www.pilvoraq.co
Target Market(s)
Business Intelligence managers, Upper level management, General managers, IT heads and graphic designers
Industry/Entity Type
Computer
Look and feel

```html
<!DOCTYPE html>
<html lang="en">
<head>
<meta charset="utf-8">
<title>Velkor Metrics — Business Card</title>
<link rel="stylesheet" href="https://fonts.googleapis.com/css2?family=Libre+Baskerville:wght@700&family=Montserrat:wght@500&family=Arimo:wght@700&display=swap">
<style>
  :root {
    --page-bg: #e4e4e4;
    --card-white: #fbfbfb;
    --card-black: #050505;
    --brand-orange: #f47b20;
    --text-white: #ffffff;
    --shadow: rgba(0, 0, 0, 0.18);
  }
  * { margin: 0; padding: 0; box-sizing: border-box; }
  html, body { width: 976px; height: 1200px; overflow: hidden; }
  body {
    background: radial-gradient(ellipse at 50% 40%, #f2f2f2 0%, var(--page-bg) 75%);
    position: relative;
  }
  .card {
    position: absolute;
    left: 88px;
    width: 800px;
    height: 457px;
    background: var(--card-white);
    box-shadow: 0 6px 18px var(--shadow);
    overflow: hidden;
  }
  .card--front { top: 100px; }
  .card--back { top: 643px; }

  .front-wave { position: absolute; inset: 0; width: 100%; height: 100%; }

  .holder { position: absolute; left: 62px; top: 52px; color: var(--text-white); }
  .holder__name {
    font-family: "Libre Baskerville", Georgia, serif;
    font-size: 34px; line-height: 1; letter-spacing: -0.5px;
  }
  .holder__role {
    font-family: "Libre Baskerville", Georgia, serif;
    font-size: 13px; letter-spacing: 5px; text-align: right; margin-top: 2px;
  }

  .contact-list {
    position: absolute; left: 62px; top: 150px; list-style: none;
    font-family: "Arimo", Arial, sans-serif; font-size: 12px;
    color: var(--text-white);
  }
  .contact-list li { display: flex; align-items: center; gap: 14px; height: 40px; }
  .contact-list svg { width: 20px; height: 20px; flex: none; fill: var(--brand-orange); }

  .brand {
    position: absolute; display: flex; align-items: center; gap: 14px;
    font-family: "Montserrat", Arial, sans-serif; font-weight: 500;
    color: var(--brand-orange); white-space: nowrap;
  }
  .brand__dot { border-radius: 50%; background: var(--brand-orange); flex: none; }
  .card--front .brand { right: 50px; top: 150px; font-size: 40px; }
  .card--front .brand__dot { width: 28px; height: 28px; }
  .card--back .brand {
    left: 50%; top: 50%; transform: translate(-50%, -50%); font-size: 46px;
  }
  .card--back .brand__dot { width: 32px; height: 32px; }
</style>
</head>
<body>
  <section class="card card--front" aria-label="Card front">
    <svg class="front-wave" viewBox="0 0 800 457" preserveAspectRatio="none" aria-hidden="true">
      <path d="M0 0 H800 V378 C660 392 560 410 430 418 C280 428 120 412 0 366 Z" fill="var(--card-black)"/>
      <path d="M0 366 C120 412 280 428 430 418 C560 410 660 392 800 378 V388 C660 400 560 418 430 426 C280 436 120 420 0 376 Z" fill="var(--brand-orange)"/>
    </svg>

    <div class="holder">
      <p class="holder__name">Tomas Arbeláez</p>
      <p class="holder__role">OWNER</p>
    </div>

    <ul class="contact-list">
      <li>
        <svg viewBox="0 0 24 24"><path d="M12 2a7 7 0 0 0-7 7c0 5 7 13 7 13s7-8 7-13a7 7 0 0 0-7-7zm0 9.5A2.5 2.5 0 1 1 12 6.5a2.5 2.5 0 0 1 0 5z"/></svg>
        <span>418 CALLE NIEVA MEDELLÍN<br>050021</span>
      </li>
      <li>
        <svg viewBox="0 0 24 24"><path d="M6.6 10.8a15 15 0 0 0 6.6 6.6l2.2-2.2a1 1 0 0 1 1-.25 11.4 11.4 0 0 0 3.6.57 1 1 0 0 1 1 1V20a1 1 0 0 1-1 1A17 17 0 0 1 3 4a1 1 0 0 1 1-1h3.5a1 1 0 0 1 1 1c0 1.25.2 2.45.57 3.57a1 1 0 0 1-.25 1z"/></svg>
        <span>0604-218-775</span>
      </li>
      <li>
        <svg viewBox="0 0 24 24"><path d="M12 2a10 10 0 1 0 0 20 10 10 0 0 0 0-20zm6.9 6h-2.9a15.7 15.7 0 0 0-1.4-3.6A8 8 0 0 1 18.9 8zM12 4a14 14 0 0 1 1.9 4h-3.8A14 14 0 0 1 12 4zM4.3 14a8 8 0 0 1 0-4h3.4a16.5 16.5 0 0 0 0 4zm.8 2h2.9a15.7 15.7 0 0 0 1.4 3.6A8 8 0 0 1 5.1 16zM8 8H5.1a8 8 0 0 1 4.3-3.6A15.7 15.7 0 0 0 8 8zm4 12a14 14 0 0 1-1.9-4h3.8A14 14 0 0 1 12 20zm2.3-6H9.7a14.7 14.7 0 0 1 0-4h4.6a14.7 14.7 0 0 1 0 4zm.3 5.6a15.7 15.7 0 0 0 1.4-3.6h2.9a8 8 0 0 1-4.3 3.6zM16.3 14a16.5 16.5 0 0 0 0-4h3.4a8 8 0 0 1 0 4z"/></svg>
        <span>www.velkormetrics.co</span>
      </li>
      <li>
        <svg viewBox="0 0 24 24"><path d="M2 5h20v14H2zm2 2v.4l8 5.2 8-5.2V7zm0 2.8V17h16V9.8l-8 5.2z"/></svg>
        <span>hola@velkormetrics.co</span>
      </li>
    </ul>

    <div class="brand">
      <span class="brand__dot" aria-hidden="true"></span>
      <span class="brand__name">Velkor Metrics</span>
    </div>
  </section>

  <section class="card card--back" aria-label="Card back">
    <div class="brand">
      <span class="brand__dot" aria-hidden="true"></span>
      <span class="brand__name">Velkor Metrics</span>
    </div>
  </section>
</body>
</html>
```